Flyer & Business Card for Lakeside Lens Guild photography courses

I need a flyer design for my company Lakeside Lens Guild - which offers photography classes for all levels in Geneva / Switzerland.

The flyer has to have an attractive visual at the front, and should highlight different types of classes and our teaching philosophy in the back.

Especially the images of Geneva (you can find some on lakesidelensguild.com and also on my photography website www.morvakimagery.com) will help to make people appreciate it's local.

Please check my website to learn more about my company, the logo, brand identity and the overall feeling:
https://www.lakesidelensguild.com

For the colors, I have used blue in the website and the logo, so it should be somehow compatible.

The final design should communicate fun courses offered by professional photographers that have received consistently 5 star ratings.

Target Market(s)

Geneva / Switzerland

Industry/Entity Type

Business

Contact Information for Business Card

Double sided - front could be a photo (or multiple photos that could be printed as part of one order from pex.com) and the back should communicate the brand identity.

Colors
0292cd
33a6d7
0555a3

```html
<!DOCTYPE html>
<html lang="en">
<head>
<meta charset="utf-8">
<title>Lakeside Lens Guild – Business Card</title>
<link href="https://fonts.googleapis.com/css2?family=Arimo:wght@700&display=swap" rel="stylesheet">
<style>
  :root {
    --page-bg: #eceeef;
    --card-white: #ffffff;
    --brand-blue: #2aa1d6;
    --brand-deep: #0555a3;
    --ink: #1d1d1f;
    --url-white: #ffffff;
  }
  html, body {
    margin: 0;
    padding: 0;
    width: 1200px;
    height: 898px;
    overflow: hidden;
    background: var(--page-bg);
  }
  .canvas {
    position: relative;
    width: 1200px;
    height: 898px;
    display: flex;
    align-items: center;
    justify-content: center;
  }
  .business-card {
    width: 840px;
    height: 480px;
    box-shadow: 0 10px 30px rgba(0, 0, 0, 0.18);
    background: var(--card-white);
  }
  .business-card svg {
    display: block;
    width: 100%;
    height: 100%;
  }
  .brand-name {
    font-family: "Arimo", Arial, sans-serif;
    font-weight: 700;
    font-size: 30px;
    fill: var(--ink);
    letter-spacing: 1px;
  }
  .card-url {
    font-family: "Arimo", Arial, sans-serif;
    font-weight: 700;
    font-size: 36px;
    fill: var(--url-white);
  }
</style>
</head>
<body>
  <main class="canvas">
    <div class="business-card">
      <svg viewBox="0 0 840 480" xmlns="http://www.w3.org/2000/svg">
        <rect class="card-base" x="0" y="0" width="840" height="480" fill="var(--card-white)"/>
        <polygon class="diagonal-band" points="0,480 840,0 840,480" fill="var(--brand-blue)"/>

        <g role="img" aria-label="Faint camera decoration in the background">
          <rect x="230" y="110" width="470" height="320" rx="44" fill="var(--brand-deep)" opacity="0.12"/>
        </g>

        <g class="brand-lockup">
          <rect x="44" y="52" width="48" height="48" fill="var(--ink)"/>
          <text class="brand-name" x="110" y="72">LAKESIDE</text>
          <text class="brand-name" x="110" y="106">LENS</text>
          <text class="brand-name" x="110" y="140">GUILD</text>
        </g>

        <text class="card-url" x="300" y="452" transform="rotate(-29.7 300 452)">www.lakesidelensguild.com</text>
      </svg>
    </div>
  </main>
</body>
</html>
```